Content developers BC and Stationary
Nubra نبراس
Content developers BC and Stationary - Corporate Services
Creative Brief
Simple
Rana T alMuttairi
Creative Director
Jeddah
rana@nubraco.com
for second partner, with Arabic on the back: Khaled Naji خالد ناجي Managing Director المدير التنفيذي +966507213690 +٩٦٦٥٠٧٢١٣٦٩٠ k@nubraco.com
رنا طارق المطيري المدير الإبداعي +٩٦٦٥٠٨٤٤١٢٥٩ rana@nubraco.com
Concepts
Business Cards and Stationery for new compliance company.
Business Cards and Stationery for Background Check Company

```html
<!DOCTYPE html>
<html lang="en">
<head>
<meta charset="utf-8">
<title>Nubra Business Card</title>
<link rel="stylesheet" href="https://fonts.googleapis.com/css2?family=Cairo:wght@400;600&family=Poppins:wght@400;500;600&display=swap">
<style>
  :root {
    --backdrop: #1e3239;
    --card: #ffffff;
    --card-shade: #eef0f3;
    --purple: #8a5cc4;
    --purple-deep: #6d3fae;
    --ink: #2c2f3a;
    --ink-soft: #6b6f7a;
  }
  * { margin: 0; padding: 0; box-sizing: border-box; }
  html, body {
    width: 1200px; height: 737px; overflow: hidden;
    background: var(--backdrop);
    font-family: "Poppins", sans-serif;
  }
  .canvas {
    width: 1200px; height: 737px;
    display: flex; align-items: center; justify-content: center; gap: 60px;
  }
  .card {
    position: relative;
    width: 520px; height: 300px;
    background: linear-gradient(160deg, var(--card) 60%, var(--card-shade));
    border-radius: 22px;
    overflow: hidden;
    box-shadow: 0 18px 40px rgba(0,0,0,.45);
  }
  .brand {
    display: flex; align-items: center; gap: 14px;
    color: var(--purple);
    font-family: "Cairo", sans-serif;
    font-weight: 600;
    line-height: 1;
  }
  .brand-ar { direction: rtl; }
  /* front */
  .card-front { padding: 30px 44px; }
  .card-front .brand { font-size: 36px; }
  .person { margin-top: 22px; }
  .person-name { font-size: 19px; font-weight: 600; color: var(--ink); line-height: 1.25; }
  .person-role { font-size: 13px; color: var(--ink-soft); margin-top: 2px; }
  .person-name-ar {
    font-family: "Cairo", sans-serif; font-size: 15px; font-weight: 600;
    color: var(--ink); direction: rtl; text-align: left; margin-top: 4px; line-height: 1.3;
  }
  .person-name-ar span { font-weight: 400; color: var(--ink-soft); font-size: 13px; }
  .contact-list { list-style: none; margin-top: 14px; }
  .contact-list li {
    display: flex; align-items: center; gap: 10px;
    font-size: 12px; color: var(--ink-soft); margin-bottom: 5px;
  }
  .contact-list svg { width: 12px; height: 12px; fill: var(--ink); flex: none; }
  /* back */
  .card-back .band { position: absolute; left: 0; top: 0; width: 140px; height: 300px; }
  .card-back .back-content {
    position: absolute; left: 170px; right: 30px; top: 0; bottom: 0;
    display: flex; flex-direction: column; justify-content: center; align-items: center; gap: 22px;
  }
  .card-back .brand { font-size: 50px; }
  .website { font-size: 15px; color: var(--ink-soft); letter-spacing: .5px; }
</style>
</head>
<body>
<main class="canvas">
  <section class="card card-front">
    <div class="brand"><span class="brand-ar" lang="ar">نبراس</span><span>Nubra</span></div>
    <div class="person">
      <div class="person-name">Rana T alMuttairi</div>
      <div class="person-role">Creative Director</div>
      <div class="person-name-ar" lang="ar">رنا طارق المطيري · <span>المدير الإبداعي</span></div>
    </div>
    <ul class="contact-list">
      <li><svg viewBox="0 0 24 24"><path d="M6.6 10.8a15 15 0 0 0 6.6 6.6l2.2-2.2a1 1 0 0 1 1-.25 11.4 11.4 0 0 0 3.6.57 1 1 0 0 1 1 1V20a1 1 0 0 1-1 1A17 17 0 0 1 3 4a1 1 0 0 1 1-1h3.5a1 1 0 0 1 1 1c0 1.25.2 2.45.57 3.57a1 1 0 0 1-.25 1z"/></svg>+966 50 844 1259</li>
      <li><svg viewBox="0 0 24 24"><path d="M2 5h20v14H2zm2 2v.5l8 5 8-5V7l-8 5z"/></svg>rana@nubraco.com</li>
      <li><svg viewBox="0 0 24 24"><path d="M12 2a7 7 0 0 0-7 7c0 5 7 13 7 13s7-8 7-13a7 7 0 0 0-7-7zm0 9.5A2.5 2.5 0 1 1 12 6.5a2.5 2.5 0 0 1 0 5z"/></svg>Office 12, Palm Road, Jeddah</li>
    </ul>
  </section>

  <section class="card card-back">
    <svg class="band" viewBox="0 0 140 300" preserveAspectRatio="none" aria-hidden="true">
      <defs>
        <linearGradient id="bandFill" x1="0" y1="0" x2="1" y2="1">
          <stop offset="0" stop-color="#9a6fd2"/>
          <stop offset="1" stop-color="#6d3fae"/>
        </linearGradient>
      </defs>
      <path d="M0 0 H110 C80 60 80 120 96 180 C108 230 120 270 126 300 H0 Z" fill="url(#bandFill)"/>
    </svg>
    <div class="back-content">
      <div class="brand"><span class="brand-ar" lang="ar">نبراس</span><span>Nubra</span></div>
      <div class="website">www.nubraco.com</div>
    </div>
  </section>
</main>
</body>
</html>
```